Pediatric Pelvic Health Brochure

Looking to design a brochure for Marlow Brook's pelvic health program. I can provide imagery once I see the layout. Our website is marlowbrookpt.example so the look should reflect that

If you see PDF titled blue and word doc you will see what we provided as thoguhts.

Target Market(s)

parents of children

Industry/Entity Type

Health And Wellness

Font styles to use
Serif

Requirements
Must have
• clear call outs - easy to read with copy,
Should not have
• not look bland or dated

```html
<!DOCTYPE html>
<html lang="en">
<head>
<meta charset="utf-8">
<title>Pediatric Pelvic Health – Marlow Brook</title>
<link rel="stylesheet" href="https://fonts.googleapis.com/css2?family=Tinos:ital,wght@0,400;1,700&family=Roboto:wght@300;400;500&family=Roboto+Condensed:wght@400&display=swap">
<style>
  :root {
    --cyan: #0bbdf0;
    --navy: #1a3a8f;
    --deep-navy: #163c8c;
    --white: #ffffff;
    --ink: #1f2a44;
    --jersey-blue: #2547b8;
    --jersey-orange: #e2602a;
  }
  * { margin: 0; padding: 0; box-sizing: border-box; }
  html, body { width: 1200px; height: 944px; overflow: hidden; background: var(--white); }
  .brochure { position: relative; width: 1200px; height: 944px; background: var(--white); font-family: "Roboto", sans-serif; }
  .top-band { position: absolute; left: 14px; top: 15px; width: 1172px; height: 28px; background: var(--cyan); }
  .bottom-band { position: absolute; left: 14px; top: 900px; width: 1172px; height: 29px; background: var(--cyan); }

  .panel { position: absolute; top: 43px; height: 857px; }
  .panel--left { left: 14px; width: 394px; background: linear-gradient(160deg, #ffffff 55%, #f1f3f6 70%, #ffffff 85%); }
  .panel--middle { left: 408px; width: 382px; background: var(--cyan); color: var(--white); }
  .panel--right { left: 790px; width: 396px; background: var(--white); }
  .panel-curve { position: absolute; left: 0; bottom: 0; }

  .diagnoses-title { position: absolute; left: 41px; top: 24px; font-family: "Tinos", serif; font-size: 31px; line-height: 32px; color: var(--navy); font-weight: 400; }
  .xray-photo { position: absolute; left: 232px; top: 59px; width: 132px; height: 132px; border-radius: 50%; border: 3px solid var(--cyan); background: linear-gradient(135deg, #f4c8cf 0%, #e56a78 40%, #c0283d 65%, #3a0a12 100%); }
  .diagnosis-list { position: absolute; left: 50px; top: 166px; list-style: none; width: 300px; }
  .diagnosis-list li { position: relative; padding-left: 40px; font-size: 17px; font-weight: 300; line-height: 21px; color: var(--ink); margin-bottom: 10px; }
  .diagnosis-list li svg { position: absolute; left: 0; top: 2px; }

  .navy-disc { position: absolute; left: 104px; top: 39px; width: 174px; height: 174px; border-radius: 50%; background: var(--deep-navy); }
  .offer { position: absolute; left: 0; top: 238px; width: 382px; text-align: center; font-family: "Roboto Condensed", sans-serif; font-size: 38px; line-height: 45px; }
  .brand { position: absolute; display: flex; align-items: center; gap: 8px; }
  .brand-mark { width: 30px; height: 30px; }
  .brand-name { font-family: "Tinos", serif; font-weight: 400; line-height: 1; }
  .brand-tag { font-family: "Tinos", serif; letter-spacing: 0.6px; text-transform: uppercase; }
  .brand--middle { left: 36px; top: 510px; }
  .brand--middle .brand-mark { background: var(--white); width: 60px; height: 64px; }
  .brand--middle .brand-name { font-size: 42px; color: var(--white); }
  .brand--middle .brand-tag { font-size: 10.5px; color: var(--white); margin-top: 2px; }
  .rule { position: absolute; left: 48px; width: 286px; height: 1px; background: var(--deep-navy); }
  .contact { position: absolute; left: 56px; display: flex; align-items: center; gap: 22px; }
  .contact--phone { top: 620px; font-size: 35px; font-weight: 500; }
  .contact--address { top: 690px; align-items: flex-start; font-size: 19.5px; line-height: 24px; }
  .contact--web { top: 780px; font-size: 20px; }

  .cover-title { font-weight: 400; }
  .title-small { position: absolute; left: 13px; top: 14px; font-family: "Tinos", serif; font-weight: 400; font-size: 40px; line-height: 44px; color: var(--navy); }
  .title-large { position: absolute; left: 13px; top: 46px; font-family: "Tinos", serif; font-weight: 400; font-size: 72px; line-height: 80px; color: var(--cyan); white-space: nowrap; }
  .players-photo { position: absolute; left: 16px; top: 117px; width: 340px; height: 510px;
    background:
      radial-gradient(ellipse 32% 40% at 40% 48%, rgba(37,71,184,0.85) 0%, rgba(37,71,184,0.35) 60%, rgba(37,71,184,0) 100%),
      radial-gradient(ellipse 30% 44% at 68% 40%, rgba(226,96,42,0.85) 0%, rgba(226,96,42,0.35) 60%, rgba(226,96,42,0) 100%),
      radial-gradient(ellipse 55% 50% at 50% 50%, #eef1f7 0%, #ffffff 100%); }
  .audience { position: absolute; left: 0; top: 632px; width: 396px; text-align: center; font-family: "Tinos", serif; font-style: italic; font-weight: 700; font-size: 28px; line-height: 33px; color: var(--navy); }
  .brand--right { left: 82px; top: 740px; }
  .brand--right .brand-mark { background: var(--deep-navy); width: 36px; height: 50px; }
  .brand--right .brand-name { font-size: 34px; color: var(--deep-navy); }
  .brand--right .brand-tag { font-size: 9px; color: var(--deep-navy); margin-top: 2px; }
  .right-web { position: absolute; left: 0; top: 826px; width: 396px; text-align: center; font-family: "Tinos", serif; font-size: 19px; color: var(--white); }
</style>
</head>
<body>
<div class="brochure">
  <div class="top-band"></div>

  <section class="panel panel--left">
    <svg class="panel-curve" width="394" height="160" viewBox="0 0 394 160"><path d="M0 28 C120 80 260 100 394 106 L394 160 L0 160 Z" fill="#0bbdf0"/></svg>
    <h2 class="diagnoses-title">We Treat a Range<br>of Diagnoses</h2>
    <div class="xray-photo" role="img" aria-label="Pelvis X-ray image"></div>
    <ul class="diagnosis-list">
      <li><svg width="20" height="18" viewBox="0 0 20 18"><path d="M1 10 L7 16 L19 1" stroke="#1a3a8f" stroke-width="3" fill="none"/></svg>Constipation</li>
      <li><svg width="20" height="18" viewBox="0 0 20 18"><path d="M1 10 L7 16 L19 1" stroke="#1a3a8f" stroke-width="3" fill="none"/></svg>Increased urinary frequency</li>
      <li><svg width="20" height="18" viewBox="0 0 20 18"><path d="M1 10 L7 16 L19 1" stroke="#1a3a8f" stroke-width="3" fill="none"/></svg>Decreased urinary frequency</li>
      <li><svg width="20" height="18" viewBox="0 0 20 18"><path d="M1 10 L7 16 L19 1" stroke="#1a3a8f" stroke-width="3" fill="none"/></svg>Day-time incontinence</li>
      <li><svg width="20" height="18" viewBox="0 0 20 18"><path d="M1 10 L7 16 L19 1" stroke="#1a3a8f" stroke-width="3" fill="none"/></svg>Night-time incontinence,</li>
      <li><svg width="20" height="18" viewBox="0 0 20 18"><path d="M1 10 L7 16 L19 1" stroke="#1a3a8f" stroke-width="3" fill="none"/></svg>bed-wetting, or enuresis</li>
      <li><svg width="20" height="18" viewBox="0 0 20 18"><path d="M1 10 L7 16 L19 1" stroke="#1a3a8f" stroke-width="3" fill="none"/></svg>Giggle incontinence</li>
      <li><svg width="20" height="18" viewBox="0 0 20 18"><path d="M1 10 L7 16 L19 1" stroke="#1a3a8f" stroke-width="3" fill="none"/></svg>Incontinence in the athletic<br>female child or teenager</li>
      <li><svg width="20" height="18" viewBox="0 0 20 18"><path d="M1 10 L7 16 L19 1" stroke="#1a3a8f" stroke-width="3" fill="none"/></svg>Waking up in the night to urinate<br>or nocturia</li>
      <li><svg width="20" height="18" viewBox="0 0 20 18"><path d="M1 10 L7 16 L19 1" stroke="#1a3a8f" stroke-width="3" fill="none"/></svg>Difficulty with urination: straining,</li>
      <li><svg width="20" height="18" viewBox="0 0 20 18"><path d="M1 10 L7 16 L19 1" stroke="#1a3a8f" stroke-width="3" fill="none"/></svg>slow flow, pain during or after<br>urination</li>
      <li><svg width="20" height="18" viewBox="0 0 20 18"><path d="M1 10 L7 16 L19 1" stroke="#1a3a8f" stroke-width="3" fill="none"/></svg>Reduced sensation of bladder or<br>bowel fullness</li>
      <li><svg width="20" height="18" viewBox="0 0 20 18"><path d="M1 10 L7 16 L19 1" stroke="#1a3a8f" stroke-width="3" fill="none"/></svg>Pain in the abdomen, bladder or<br>lower back</li>
      <li><svg width="20" height="18" viewBox="0 0 20 18"><path d="M1 10 L7 16 L19 1" stroke="#1a3a8f" stroke-width="3" fill="none"/></svg>Fecal incontinence</li>
      <li><svg width="20" height="18" viewBox="0 0 20 18"><path d="M1 10 L7 16 L19 1" stroke="#1a3a8f" stroke-width="3" fill="none"/></svg>Treatment after pediatric pelvic<br>Surgeries</li>
    </ul>
  </section>

  <section class="panel panel--middle">
    <div class="navy-disc"></div>
    <p class="offer">We offer a FREE 15<br>minute consultation to<br>help you determine if<br>physical therapy is<br>right for you.</p>
    <div class="brand brand--middle">
      <div class="brand-mark"></div>
      <div><div class="brand-name">Marlow Brook</div><div class="brand-tag">Physical and Aquatic Therapy</div></div>
    </div>
    <div class="rule" style="top:609px"></div>
    <div class="contact contact--phone">
      <svg width="34" height="34" viewBox="0 0 24 24"><path fill="#fff" d="M6.6 10.8a15.1 15.1 0 0 0 6.6 6.6l2.2-2.2a1 1 0 0 1 1-.25 11.4 11.4 0 0 0 3.6.57 1 1 0 0 1 1 1V20a1 1 0 0 1-1 1A17 17 0 0 1 3 4a1 1 0 0 1 1-1h3.5a1 1 0 0 1 1 1c0 1.250.2 2.45.57 3.57a1 1 0 0 1-.25 1z"/></svg>
      <span>212.555.0147</span>
    </div>
    <div class="rule" style="top:680px"></div>
    <div class="contact contact--address">
      <svg width="28" height="38" viewBox="0 0 24 32"><path fill="#fff" d="M12 0a11 11 0 0 0-11 11c0 8 11 21 11 21s11-13 11-21A11 11 0 0 0 12 0zm0 15a4 4 0 1 1 0-8 4 4 0 0 1 0 8z"/></svg>
      <span>48 Linden Avenue<br>Ground Floor<br>New York, NY 10022</span>
    </div>
    <div class="rule" style="top:769px"></div>
    <div class="contact contact--web">
      <svg width="36" height="36" viewBox="0 0 36 36" fill="none" stroke="#fff" stroke-width="1.6"><circle cx="18" cy="18" r="16"/><ellipse cx="18" cy="18" rx="7" ry="16"/><path d="M2 18h32M5 10h26M5 26h26M18 2v32"/></svg>
      <span>marlowbrookpt.example</span>
    </div>
  </section>

  <section class="panel panel--right">
    <div class="players-photo" role="img" aria-label="Two teenage boys in blue and orange jerseys playing basketball"></div>
    <h1 class="cover-title"><span class="title-small">Pediatric</span><span class="title-large">Pelvic Health</span></h1>
    <svg class="panel-curve" width="396" height="120" viewBox="0 0 396 120"><path d="M0 85 C150 82 300 72 396 47 L396 120 L0 120 Z" fill="#0bbdf0"/></svg>
    <p class="audience">Treating Infants<br>Children<br>&amp; Adolescents</p>
    <div class="brand brand--right">
      <div class="brand-mark"></div>
      <div><div class="brand-name">Marlow Brook</div><div class="brand-tag">Physical and Aquatic Therapy</div></div>
    </div>
    <p class="right-web">marlowbrookpt.example</p>
  </section>

  <div class="bottom-band"></div>
</div>
</body>
</html>
```